design a construction company business card

Design business card around our logo. Card must have all the typical info: name, title, address, phone, email, business name, etc. Somewhere on the card I would like to see our motto "Built on integrity... Inspired by commitment." Consider adding a splash of bright orange to the card to complement the blues and silvers/grays in the logo. We are open to metallic inks, textures, etc. We would like to see options on both light and dark backgrounds. The font in the logo is Euro Technic Extended Regular.

```html
<!DOCTYPE html>
<html lang="en">
<head>
<meta charset="utf-8">
<title>Harlow Contracting – Business Card</title>
<link rel="stylesheet" href="https://fonts.googleapis.com/css2?family=Nunito:wght@400;600&display=swap">
<style>
  :root {
    --brand-blue: #17488a;
    --ink-white: #ffffff;
    --night: #161825;
    --sheet-light: #ffffff;
    --sheet-dark: #060607;
    --accent-orange: #f05a22;
    --glow-orange: #f9b68c;
    --card-shadow: rgba(0,0,0,0.18);
  }
  * { margin: 0; padding: 0; box-sizing: border-box; }
  html, body { width: 1200px; height: 972px; overflow: hidden; }
  body { position: relative; font-family: "Nunito", sans-serif; }

  .sheet { position: absolute; left: 0; width: 1200px; }
  .sheet--light { top: 0; height: 479px; background: var(--sheet-light); }
  .sheet--dark { top: 479px; height: 493px; background: var(--sheet-dark); }

  .card { position: absolute; width: 560px; height: 320px; overflow: hidden; }
  .card--front { left: 32px; background: var(--ink-white); box-shadow: 0 0 4px var(--card-shadow); }
  .card--back { left: 622px; width: 559px; background: var(--night); }
  .sheet--light .card { top: 98px; }
  .sheet--dark .card { top: 90px; }

  .card__shapes { position: absolute; inset: 0; }

  .contact { position: absolute; left: 19px; top: 0; color: var(--ink-white); }
  .contact__name { position: absolute; top: 42px; font-size: 26px; font-weight: 400; white-space: nowrap; letter-spacing: 0.3px; }
  .contact__post { position: absolute; top: 77px; font-size: 15px; white-space: nowrap; }
  .contact__row { position: absolute; left: 0; display: flex; align-items: flex-start; gap: 7px; font-size: 15px; line-height: 19px; white-space: nowrap; }
  .contact__row svg { width: 17px; height: 17px; margin-top: 1px; flex: none; }
  .row--phone { top: 119px; }
  .row--mail { top: 152px; }
  .row--web { top: 188px; }
  .row--pin { top: 222px; }

  .brand-glow {
    position: absolute; left: 360px; top: 50px; width: 160px; height: 160px; border-radius: 50%;
    background: radial-gradient(circle, var(--glow-orange) 0%, rgba(249,182,140,0.55) 45%, rgba(249,182,140,0) 72%);
  }
  .brand-name {
    position: absolute; text-align: center; color: var(--brand-blue);
    font-weight: 600; text-transform: uppercase; line-height: 1.15;
  }
  .card--front .brand-name { left: 330px; width: 220px; top: 108px; font-size: 24px; letter-spacing: 2px; }
  .card--back .brand-name { left: 150px; width: 260px; top: 82px; font-size: 27px; letter-spacing: 2px; color: #2a5bb0; }
  .brand-name small { display: block; font-size: 12px; letter-spacing: 2.5px; }

  .motto {
    position: absolute; left: 0; width: 100%; top: 188px; text-align: center;
    color: var(--accent-orange); font-size: 23px; line-height: 30px;
  }
</style>
</head>
<body>

<section class="sheet sheet--light">
  <div class="card card--front">
    <svg class="card__shapes" viewBox="0 0 560 320" aria-hidden="true">
      <polygon fill="var(--brand-blue)" points="0,0 280,0 295,14 295,38 285,46 285,274 295,282 295,306 280,320 0,320"/>
      <polygon fill="var(--ink-white)" points="236,136 280,110 280,211 236,186"/>
      <polygon fill="var(--brand-blue)" points="280,113 325,138 325,186 280,211"/>
      <polygon fill="var(--brand-blue)" points="560,0 560,320 555,320 542,308 542,276 552,268 552,52 542,44 542,12 555,0"/>
    </svg>
    <div class="contact">
      <div class="contact__name">Jhon Deo</div>
      <div class="contact__post">Your Post Here</div>
      <div class="contact__row row--phone"><svg viewBox="0 0 24 24" fill="none" stroke="#fff" stroke-width="1.4"><path d="M5 3l4 1 1 5-2 1.5a12 12 0 0 0 6 6L15.5 14l5 1 1 4-2 2C11 21 3 13 3 5z"/></svg>(+22)1234 567 890</div>
      <div class="contact__row row--mail"><svg viewBox="0 0 24 24" fill="none" stroke="#fff" stroke-width="1.4"><rect x="2.5" y="5" width="19" height="14"/><path d="M2.5 5l9.5 8 9.5-8M2.5 19l7-6.5M21.5 19l-7-6.5"/></svg>harlowbuild@mail.com</div>
      <div class="contact__row row--web"><svg viewBox="0 0 24 24" fill="none" stroke="#fff" stroke-width="1.4"><circle cx="12" cy="12" r="9.5"/><ellipse cx="12" cy="12" rx="4.5" ry="9.5"/><path d="M2.5 12h19M4 7h16M4 17h16"/></svg>www.companyweb.com</div>
      <div class="contact__row row--pin"><svg viewBox="0 0 24 24" fill="none" stroke="#fff" stroke-width="1.4"><path d="M12 22s-7-7-7-12a7 7 0 0 1 14 0c0 5-7 12-7 12z"/><circle cx="12" cy="10" r="3"/></svg><span>address, street name, city,<br>pin cord, country</span></div>
    </div>
    <div class="brand-glow"></div>
    <div class="brand-name">Harlow<small>Contracting, Inc.</small></div>
  </div>

  <div class="card card--back">
    <div class="brand-name">Harlow<small>Contracting, Inc.</small></div>
    <p class="motto">Built on integrity<br>Inspired by commitment.</p>
  </div>
</section>

<section class="sheet sheet--dark">
  <div class="card card--front">
    <svg class="card__shapes" viewBox="0 0 560 320" aria-hidden="true">
      <polygon fill="var(--brand-blue)" points="0,0 280,0 295,14 295,38 285,46 285,274 295,282 295,306 280,320 0,320"/>
      <polygon fill="var(--ink-white)" points="236,136 280,110 280,211 236,186"/>
      <polygon fill="var(--brand-blue)" points="280,113 325,138 325,186 280,211"/>
      <polygon fill="var(--brand-blue)" points="560,0 560,320 555,320 542,308 542,276 552,268 552,52 542,44 542,12 555,0"/>
    </svg>
    <div class="contact">
      <div class="contact__name">Jhon Deo</div>
      <div class="contact__post">Your Post Here</div>
      <div class="contact__row row--phone"><svg viewBox="0 0 24 24" fill="none" stroke="#fff" stroke-width="1.4"><path d="M5 3l4 1 1 5-2 1.5a12 12 0 0 0 6 6L15.5 14l5 1 1 4-2 2C11 21 3 13 3 5z"/></svg>(+22)1234 567 890</div>
      <div class="contact__row row--mail"><svg viewBox="0 0 24 24" fill="none" stroke="#fff" stroke-width="1.4"><rect x="2.5" y="5" width="19" height="14"/><path d="M2.5 5l9.5 8 9.5-8M2.5 19l7-6.5M21.5 19l-7-6.5"/></svg>harlowbuild@mail.com</div>
      <div class="contact__row row--web"><svg viewBox="0 0 24 24" fill="none" stroke="#fff" stroke-width="1.4"><circle cx="12" cy="12" r="9.5"/><ellipse cx="12" cy="12" rx="4.5" ry="9.5"/><path d="M2.5 12h19M4 7h16M4 17h16"/></svg>www.companyweb.com</div>
      <div class="contact__row row--pin"><svg viewBox="0 0 24 24" fill="none" stroke="#fff" stroke-width="1.4"><path d="M12 22s-7-7-7-12a7 7 0 0 1 14 0c0 5-7 12-7 12z"/><circle cx="12" cy="10" r="3"/></svg><span>address, street name, city,<br>pin cord, country</span></div>
    </div>
    <div class="brand-glow"></div>
    <div class="brand-name">Harlow<small>Contracting, Inc.</small></div>
  </div>

  <div class="card card--back">
    <div class="brand-name">Harlow<small>Contracting, Inc.</small></div>
    <p class="motto">Built on integrity<br>Inspired by commitment.</p>
  </div>
</section>

</body>
</html>
```